Marieke ten Hoorn Interior Designer

I have been designing for 25 years and it's now time for a change of look to my business card. My business name is Lumivale Studio (Lumivale Holdings Ltd), however, I would prefer to use my own name as the brand instead, in a memorable way (to go through the entire business re-branding process after 20 years would be difficult so I need to retain the business name somewhere on the card) I would like my business name in small print on the rear of the card. I would like to convey that I am a creative award winning interior designer and that I do other property projects, I can supply furnishings, colour schemes. I prefer simple fonts/simple look to the card. I need to appeal to Residential high end, commercial clients and hospitality. I would prefer a 1-3 colour graphic. Have a look at my website: www.lvstudio.co.nz, Chatterbook: Lumivale Studio, Roomtrek.com: Marieke ten Hoorn to see examples of my work.
Updates

Hello I am happy for this design project timeframe to be extended to a week so please feel free to take a little more time. thanks.

Thank you to all the designers who submitted their designs - I appreciate your efforts and I am sorry that I cannot choose more than one design. Thank you again.

Industry/Entity Type

Architecture

Contact Information for Business Card

My details are: email - Marieke@lvstudio.co.nz, Web: www.lvstudio.co.nz, Address: Locations in Wellington and Kapiti, New Zealand. I would prefer not to have my postal address on the card as it is not an office or a place that is open to the public so I have not included that information here.

Font styles to use
Serif
Sans Serif

Colors

Designer to choose colors to be used in the design.

Requirements
Must have
• a reference to my being a Creative Award Winning Interior Designer with experience in Residential, commercial, hospitality design. on the back of the card it needs to say my business name: Lumivale Studio and the words "Locations in Wellington and Kapiti".
Nice to have
• A clean, memorable card with a clear message - not too much information.
Should not have
• I do not want an over detailed business card. I also don't want to use our existing logo - I have used it for 20 years and I am tired of it so I would like to use my name as a brand instead.

```html
<!DOCTYPE html>
<html lang="en">
<head>
<meta charset="utf-8">
<title>Marieke ten Hoorn — Business Card</title>
<link rel="stylesheet" href="https://fonts.googleapis.com/css2?family=Lato:wght@400;700&display=swap">
<style>
  :root {
    --backdrop: #e9e7e3;
    --card: #ffffff;
    --ink: #2e3038;
    --ink-soft: #4a4c55;
    --taupe: #8b7f66;
    --shadow: rgba(0, 0, 0, 0.18);
  }
  * { box-sizing: border-box; margin: 0; padding: 0; }
  html, body {
    width: 1200px;
    height: 912px;
    overflow: hidden;
    background: var(--backdrop);
    font-family: "Lato", sans-serif;
    color: var(--ink);
  }
  .canvas { position: relative; width: 1200px; height: 912px; }
  .card {
    position: absolute;
    width: 640px;
    height: 366px;
    background: var(--card);
    box-shadow: 0 10px 28px var(--shadow);
  }
  .card--front { left: 150px; top: 70px; }
  .card--back  { left: 410px; top: 476px; }

  .brand {
    position: absolute;
    display: flex;
    align-items: center;
    gap: 14px;
    font-weight: 700;
    color: var(--ink);
    letter-spacing: 0.03em;
    white-space: nowrap;
  }
  .brand__dot { border-radius: 50%; background: var(--taupe); flex: none; }

  .card--front .brand {
    left: 50%; top: 50%;
    transform: translate(-50%, -50%);
    font-size: 44px;
  }
  .card--front .brand__dot { width: 34px; height: 34px; }

  .business {
    position: absolute;
    left: 48px;
    top: 183px;
    transform: translateY(-50%);
  }
  .business .brand { position: static; font-size: 24px; gap: 12px; }
  .business .brand__dot { width: 20px; height: 20px; }
  .business__entity {
    margin: 6px 0 0 32px;
    font-size: 11px;
    color: var(--ink-soft);
    letter-spacing: 0.05em;
  }
  .business__locations {
    margin: 4px 0 0 32px;
    font-size: 12px;
    color: var(--taupe);
  }

  .contact {
    position: absolute;
    left: 380px;
    top: 64px;
    color: var(--ink-soft);
  }
  .contact__name { font-size: 21px; font-weight: 400; color: var(--ink); line-height: 1.1; }
  .contact__role { font-size: 12px; margin: 2px 0 0 22px; }
  .contact__expertise { font-size: 13px; line-height: 1.35; margin: 20px 0 0 22px; }
  .contact__list { list-style: none; margin: 20px 0 0 22px; }
  .contact__item {
    display: flex;
    align-items: center;
    gap: 10px;
    font-size: 13px;
    height: 24px;
  }
  .contact__icon { width: 18px; height: 18px; flex: none; }
</style>
</head>
<body>
<main class="canvas">

  <section class="card card--front" aria-label="Card front">
    <div class="brand">
      <span class="brand__dot"></span>
      <span class="brand__name">Marieke ten Hoorn</span>
    </div>
  </section>

  <section class="card card--back" aria-label="Card back">
    <div class="business">
      <div class="brand">
        <span class="brand__dot"></span>
        <span class="brand__name">Lumivale Studio</span>
      </div>
      <p class="business__entity">Lumivale Holdings Ltd</p>
      <p class="business__locations">Locations in Wellington and Kapiti</p>
    </div>

    <div class="contact">
      <h1 class="contact__name">Marieke ten Hoorn</h1>
      <p class="contact__role">Interior Designer</p>
      <p class="contact__expertise">
        Creative Award Winning Design<br>
        Residential, Commercial, Hospitality
      </p>
      <ul class="contact__list">
        <li class="contact__item">
          <svg class="contact__icon" viewBox="0 0 18 18" aria-hidden="true">
            <circle cx="9" cy="9" r="8" fill="none" stroke="var(--taupe)" stroke-width="1.3"/>
            <path d="M6.3 5.2c.4-.3.9-.2 1.1.2l.6 1.2c.2.3.1.7-.2.9l-.5.4c.4.9 1.1 1.6 2 2l.4-.5c.2-.3.6-.4.9-.2l1.2.6c.4.2.5.7.2 1.1l-.5.7c-.4.5-1.1.6-1.7.3-1.9-.9-3.3-2.3-4.2-4.2-.3-.6-.2-1.3.3-1.7z" fill="var(--taupe)"/>
          </svg>
          <span>+6420555017</span>
        </li>
        <li class="contact__item">
          <svg class="contact__icon" viewBox="0 0 18 18" aria-hidden="true">
            <circle cx="9" cy="9" r="8" fill="none" stroke="var(--taupe)" stroke-width="1.3"/>
            <rect x="4.8" y="6" width="8.4" height="6" rx="0.6" fill="var(--taupe)"/>
            <path d="M5 6.3l4 3 4-3" fill="none" stroke="#fff" stroke-width="0.9"/>
          </svg>
          <span>Marieke@lvstudio.co.nz</span>
        </li>
        <li class="contact__item">
          <svg class="contact__icon" viewBox="0 0 18 18" aria-hidden="true">
            <circle cx="9" cy="9" r="8" fill="none" stroke="var(--taupe)" stroke-width="1.3"/>
            <circle cx="9" cy="9" r="4.6" fill="none" stroke="var(--taupe)" stroke-width="1"/>
            <ellipse cx="9" cy="9" rx="2" ry="4.6" fill="none" stroke="var(--taupe)" stroke-width="0.9"/>
            <path d="M4.4 9h9.2" stroke="var(--taupe)" stroke-width="0.9"/>
          </svg>
          <span>www.lvstudio.co.nz</span>
        </li>
      </ul>
    </div>
  </section>

</main>
</body>
</html>
```